business card

Business card for new business.
Red and black corporate colors.
Card can have an Indsutrial feel to it. Feel free to add Rust, Bolted steel, or graphics as you see fit. We provide highly specialized services to the below mentioned industries.
Keep information out of corners so that if I want I can choose rounded corners.
Information
- front. name - title - phone - email
- Rear
Welding - Piping - Fabrication - Rigging - Coatings
Regina - Saskatoon - Red Deer - Kamloops - Prince George

```html
<!DOCTYPE html>
<html lang="en">
<head>
<meta charset="utf-8">
<title>Framewell business card</title>
<link rel="stylesheet" href="https://fonts.googleapis.com/css2?family=Roboto:wght@400;500;900&display=swap">
<style>
  :root {
    --page: #e4e4e6;
    --card-white: #ffffff;
    --card-white-shade: #ececec;
    --card-grey: #6a6a6d;
    --card-grey-dark: #5a5a5d;
    --map-tone: #7a7a7d;
    --red: #d8141c;
    --ink: #555558;
    --ink-soft: #6e6e72;
    --on-grey: #d6d6d8;
  }
  * { box-sizing: border-box; margin: 0; padding: 0; }
  html, body { width: 1200px; height: 900px; overflow: hidden; }
  body {
    background: var(--page);
    font-family: "Roboto", Arial, sans-serif;
    position: relative;
  }
  .card {
    position: absolute;
    left: 250px;
    width: 700px;
    height: 400px;
    border-radius: 22px;
    overflow: hidden;
    box-shadow: 0 10px 28px rgba(0,0,0,0.25);
  }
  .card-front {
    top: 36px;
    background: radial-gradient(ellipse at 70% 25%, var(--card-white) 45%, var(--card-white-shade) 100%);
  }
  .brand-mark {
    position: absolute;
    top: 70px;
    right: 70px;
    display: flex;
    align-items: center;
    gap: 12px;
  }
  .brand-square {
    width: 26px;
    height: 26px;
    background: var(--red);
  }
  .brand-name {
    font-weight: 900;
    font-size: 44px;
    letter-spacing: 1px;
    color: var(--ink);
  }
  .holder {
    position: absolute;
    left: 70px;
    top: 190px;
  }
  .holder-name {
    font-size: 26px;
    font-weight: 400;
    color: var(--red);
    letter-spacing: 0.5px;
  }
  .holder-title {
    font-size: 15px;
    color: var(--ink-soft);
    margin-top: 2px;
  }
  .divider {
    position: absolute;
    left: 70px;
    right: 70px;
    top: 262px;
    height: 1px;
    background: var(--red);
  }
  .contact {
    position: absolute;
    left: 70px;
    top: 280px;
    font-size: 15px;
    line-height: 26px;
    color: var(--ink-soft);
  }
  .contact .label { color: var(--red); font-weight: 500; }
  .contact .accent { color: var(--red); }
  .card-back {
    top: 466px;
    background: linear-gradient(160deg, var(--card-grey) 0%, var(--card-grey-dark) 100%);
  }
  .world-map {
    position: absolute;
    left: 60px;
    top: 40px;
    width: 580px;
    height: 320px;
    border-radius: 40px;
    background: radial-gradient(ellipse at center, var(--map-tone) 0%, rgba(122,122,125,0) 70%);
  }
  .back-brand {
    position: absolute;
    top: 95px;
    left: 0;
    right: 0;
    display: flex;
    justify-content: center;
    align-items: center;
    gap: 16px;
  }
  .back-brand .brand-square { width: 34px; height: 34px; background: var(--on-grey); }
  .back-brand .brand-name { font-size: 62px; color: var(--on-grey); }
  .services {
    position: absolute;
    top: 230px;
    left: 0;
    right: 0;
    text-align: center;
    color: var(--on-grey);
    font-size: 18px;
    line-height: 30px;
  }
</style>
</head>
<body>
  <section class="card card-front">
    <div class="brand-mark">
      <span class="brand-square"></span>
      <span class="brand-name">FRAMEWELL</span>
    </div>
    <div class="holder">
      <h1 class="holder-name">JORDAN KELLER</h1>
      <p class="holder-title">Director</p>
    </div>
    <div class="divider"></div>
    <div class="contact">
      <p><span class="label">P :</span> +330 5172-4406 | <span class="label">E :</span> info@framewell.com | <span class="label">W :</span> www.<span class="accent">framewell</span>.com</p>
      <p>2190 Quarry Ridge Rd. Austin, TX 78745</p>
    </div>
  </section>

  <section class="card card-back">
    <div class="world-map" role="img" aria-label="Faint dotted world map in the background"></div>
    <div class="back-brand">
      <span class="brand-square"></span>
      <span class="brand-name">FRAMEWELL</span>
    </div>
    <div class="services">
      <p>Welding - Piping - Fabrication - Rigging - Coatings</p>
      <p>Regina - Saskatoon - Red Deer - Kamloops - Prince George</p>
    </div>
  </section>
</body>
</html>
```